Rock Band needs a CD Cover for the next album

We’re looking for a CD cover design for our next rock album to be released in summer 2016.

We are 2 guys based in Switzerland writing and recording the songs and all it’s instruments ourselves. Feel free to take a look at us and our previous work on www.hollowlantern.net.

The next album is to be called ‘Lullabies keep the river cold’ and we would like to have the artwork also represent the album name. It should contain a link or resemblance to anything out of the fairytale Tobin Quill. In addition to the fairytales link, we would also like to have the ‘rock-music’ style in there, with that I mean not too bright colours, more darkish, maybe even mystic. We’re open for any ideas you guys may have.

Target Market(s)

rock Music fans, Young and old, all genders

Requirements
Must have
• - Band name must be on the cover: Hollow Lantern
• - Album Title must be on the cover: Lullabies keep the river cold

```html
<!DOCTYPE html>
<html lang="en">
<head>
<meta charset="utf-8">
<title>Hollow Lantern – Lullabies keep the river cold</title>
<link rel="stylesheet" href="https://fonts.googleapis.com/css2?family=Bungee&family=Bungee+Outline&display=swap">
<style>
  :root {
    --sky-deep: #3a2c00;
    --sky-mid: #8a6a05;
    --sky-glow: #e2b21c;
    --night: #000000;
    --ink: #ffffff;
  }
  html, body {
    margin: 0;
    padding: 0;
    width: 1200px;
    height: 1200px;
    overflow: hidden;
    background: var(--night);
  }
  .cover {
    position: relative;
    width: 1200px;
    height: 1200px;
    background: var(--night);
    overflow: hidden;
  }
  .sky-scene {
    position: absolute;
    left: 0;
    top: 0;
    width: 1200px;
    height: 600px;
    background:
      radial-gradient(circle at 940px 150px, #ffe58a 0, #f0c437 150px, rgba(226,178,28,0) 260px),
      linear-gradient(180deg, var(--sky-deep) 0%, var(--sky-mid) 55%, var(--sky-glow) 100%);
  }
  .title-art {
    position: absolute;
    left: 0;
    top: 0;
    width: 1200px;
    height: 1200px;
  }
  .album-title {
    font-family: "Bungee Outline", sans-serif;
    font-size: 70px;
    fill: var(--ink);
  }
  .band-name {
    font-family: "Bungee", sans-serif;
    font-size: 46px;
    fill: var(--ink);
  }
</style>
</head>
<body>
  <main class="cover">
    <div class="sky-scene" role="img" aria-label="Golden night sky with a large half moon and billowing clouds"></div>

    <svg class="title-art" viewBox="0 0 1200 1200" xmlns="http://www.w3.org/2000/svg">
      <g class="title-block" transform="translate(555 1058) rotate(-35)">
        <text class="album-title" x="0" y="-72" textLength="600" lengthAdjust="spacingAndGlyphs">LULLABIES KEEP</text>
        <text class="album-title" x="0" y="0" textLength="600" lengthAdjust="spacingAndGlyphs">THE RIVER COLD</text>
        <text class="band-name" x="70" y="60" textLength="490" lengthAdjust="spacingAndGlyphs">HOLLOW LANTERN</text>
      </g>
    </svg>
  </main>
</body>
</html>
```